Our company, Brisk Ladle Pantry prepares handmade, wholesome meals fully cooked and ready to he...

We are rolling out a line of Artisan Small Batch Salad dressings. Our initial offering is an herb/Dijon based vinaigrette that has pleased our friends and families for years. We would like to see designs that incorporate the colors in our logo ( Green is 107 165 57, Gray is 72 72 74 ) The final design should communicate freshness, herbs ( parsley, onion, lettuce, cherry tomatoes, olives) that are caricatures or line drawings at the top or left side of the label. Some or all of these veggies can be used depending upon space,layout etc. Space should not be crowded. Note: We anticipate having additional offerings in the future under the "brisk toppings" name such as sauces and marinades. The attached drawing is only a concept drawing and we defer to the designer for layout and creativity. Our company name is Brisk Ladle Pantry and we would like to incorporate a "fork" in this label design

Font styles to use
Decorative
Script

Colors

Designer to choose colors to be used in the design.

Requirements
Must have
• Vegetables should be in a caricature or line drawing format.
Nice to have
• I uploaded an MS word document that contains a head shot photo of the owner. We would like to have a whimsical rendition done that we will add to our left or right panel on the label.

```html
<!DOCTYPE html>
<html lang="en">
<head>
<meta charset="utf-8">
<title>Brisk Ladle Pantry – Artisan Vinaigrette Label</title>
<link rel="stylesheet" href="https://fonts.googleapis.com/css2?family=Cinzel:wght@600;700&family=Great+Vibes&family=Roboto:ital,wght@0,300;0,400;0,700;1,700&family=Roboto+Condensed:wght@400;700&display=swap">
<style>
  :root {
    --brand-green: #6ba539;
    --green-light: #7cb547;
    --brand-gray: #48484a;
    --mid-gray: #8c8c8e;
    --text-gray: #8e8e90;
    --stripe-gray: #ededed;
    --stripe-gray-2: #f7f7f7;
    --coral: #ef6a57;
    --mustard: #e5d23a;
    --white: #ffffff;
    --stage: #e3e3e4;
  }
  * { box-sizing: border-box; margin: 0; padding: 0; }
  html, body { width: 1028px; height: 1200px; overflow: hidden; }
  body { background: var(--stage); font-family: "Roboto", Arial, sans-serif; position: relative; }

  .label {
    position: absolute; left: 24px; top: 349px; width: 980px; height: 502px;
    background: var(--white); overflow: hidden;
    box-shadow: 0 6px 14px rgba(0,0,0,.18);
  }
  .label > * { position: absolute; }

  /* top band */
  .top-band { left: 0; top: 0; width: 980px; height: 104px; background: var(--mid-gray); }
  .herb-art-left { left: 250px; top: 0; width: 110px; height: 104px; background: linear-gradient(90deg, #8c8c8e, #a2a2a4); }
  .veg-art-right { left: 621px; top: 0; width: 359px; height: 104px; background: linear-gradient(90deg, #9a9a9c, #a9a9ab 50%, #959597); }
  .portrait {
    left: 14px; top: 5px; width: 120px; height: 120px; border-radius: 50%;
    background: radial-gradient(circle at 50% 45%, #f4f4f4, #b9b9ba 70%, #7a7a7c);
    border: 3px solid #6f6f71; z-index: 2;
  }
  .founder-name {
    left: 112px; top: 46px; font-family: "Great Vibes", cursive; font-size: 30px; line-height: 34px;
    color: var(--white); transform: rotate(-15deg); transform-origin: left center; white-space: nowrap;
  }
  .founder-role { left: 136px; top: 84px; font-family: "Roboto Condensed", Arial, sans-serif; font-size: 15px; color: var(--white); letter-spacing: .5px; }

  .logo-arch {
    left: 360px; top: 0; width: 261px; height: 102px; background: var(--white);
    border-top-left-radius: 70px 80px; border-top-right-radius: 70px 80px;
    display: flex; flex-direction: column; align-items: center; justify-content: center; gap: 6px;
  }
  .logo-mark { width: 22px; height: 22px; border-radius: 50%; background: var(--brand-green); }
  .logo-name { font-family: "Roboto", Arial, sans-serif; font-weight: 700; font-size: 19px; color: var(--brand-gray); letter-spacing: .3px; }

  /* green stripes */
  .stripe-band {
    left: 0; top: 102px; width: 980px; height: 34px;
    background: repeating-linear-gradient(180deg, var(--brand-green) 0 4px, var(--green-light) 4px 8px);
  }
  .line-name { left: 360px; top: 104px; width: 261px; text-align: center; font-family: "Great Vibes", cursive; font-size: 34px; line-height: 40px; color: var(--white); z-index: 2; }

  /* body */
  .story { left: 13px; top: 158px; width: 240px; font-size: 13.5px; line-height: 15.6px; color: var(--brand-green); font-weight: 300; }
  .story p + p { margin-top: 10px; }
  .story strong { font-weight: 400; }

  .title { left: 250px; top: 144px; width: 482px; text-align: center; font-family: "Cinzel", Georgia, serif; font-weight: 700; }
  .title-top { font-size: 58px; color: var(--coral); line-height: 62px; position: relative; }
  .title-top::before, .title-top::after { content: ""; position: absolute; top: 32px; width: 56px; height: 2px; background: var(--brand-green); }
  .title-top::before { left: 10px; } .title-top::after { right: 10px; }
  .title-main { font-size: 60px; color: var(--mustard); line-height: 60px; letter-spacing: -1px; }
  .title-rule { left: 270px; top: 298px; width: 442px; height: 2px; background: var(--brand-green); }

  .marinade-band {
    left: 0; top: 306px; width: 980px; height: 42px;
    background: repeating-linear-gradient(180deg, var(--brand-green) 0 4px, var(--green-light) 4px 8px);
    clip-path: polygon(0 100%, 0 60%, 25% 20%, 50% 0, 75% 20%, 100% 60%, 100% 100%);
  }
  .marinade { left: 360px; top: 320px; width: 261px; text-align: center; font-family: "Cinzel", Georgia, serif; font-weight: 700; font-size: 22px; line-height: 26px; color: var(--white); }

  .ingredients {
    left: 750px; top: 150px; width: 44px; height: 150px;
    writing-mode: vertical-rl; transform: rotate(180deg);
    font-size: 10.5px; line-height: 13px; color: var(--brand-green);
  }
  .nutrition-panel { left: 805px; top: 136px; width: 175px; height: 196px; background: repeating-linear-gradient(180deg, var(--brand-green) 0 4px, var(--green-light) 4px 8px); z-index: 2; }
  .nutrition {
    left: 814px; top: 142px; width: 156px; height: 184px; border: 1px solid var(--white); z-index: 3;
    padding: 3px 4px; color: var(--white); font-family: "Roboto Condensed", Arial, sans-serif; font-size: 7.3px; line-height: 8.9px;
  }
  .nutrition .row { display: flex; justify-content: space-between; }
  .nutrition .indent { padding-left: 5px; }
  .nutrition b { font-weight: 700; }
  .nutrition .rule { border-top: 1px solid var(--white); margin: 2px 0; }

  /* lower section */
  .gray-bar { left: 0; top: 348px; width: 980px; height: 20px; background: var(--mid-gray); z-index: 3; }
  .green-bar { left: 0; top: 368px; width: 980px; height: 8px; background: var(--brand-green); z-index: 3; }
  .lower-stripes { left: 0; top: 376px; width: 980px; height: 126px; background: repeating-linear-gradient(180deg, var(--stripe-gray) 0 3px, var(--stripe-gray-2) 3px 6px); }
  .salad-art {
    left: 418px; top: 360px; width: 195px; height: 118px; border-radius: 50%; z-index: 4;
    background: radial-gradient(ellipse at 50% 45%, #7fb44a 0 40%, #c9d98a 55%, #f3f3f3 70%, #e0e0e0 100%);
  }
  .fork-art { left: 610px; top: 372px; width: 60px; height: 110px; z-index: 4; background: linear-gradient(135deg, transparent 45%, #bdbdbd 48% 52%, transparent 55%); }

  .care-left { left: 13px; top: 394px; font-size: 13px; line-height: 17px; color: var(--text-gray); }
  .thanks { left: 13px; top: 447px; font-size: 13px; line-height: 17px; color: var(--brand-green); font-style: italic; font-weight: 700; }
  .net { left: 620px; top: 447px; width: 82px; text-align: center; font-size: 13px; line-height: 17px; color: var(--text-gray); font-weight: 700; z-index: 5; }
  .care-right { right: 15px; top: 398px; text-align: right; font-size: 14px; line-height: 17px; color: var(--brand-gray); }
  .care-right .web { color: var(--brand-green); font-style: italic; font-weight: 700; display: block; }
  .care-right .storage { color: var(--text-gray); margin-top: 6px; }
</style>
</head>
<body>
  <div class="label">
    <div class="top-band"></div>
    <div class="herb-art-left" role="img" aria-label="Line drawing of olive branch"></div>
    <div class="veg-art-right" role="img" aria-label="Line drawings of lettuce, tomatoes, onion and parsley"></div>
    <div class="portrait" role="img" aria-label="Whimsical portrait of the co-founder"></div>
    <div class="founder-name">Walt Hensley</div>
    <div class="founder-role">CO-FOUNDER</div>

    <div class="stripe-band"></div>
    <div class="logo-arch">
      <span class="logo-mark"></span>
      <span class="logo-name">BRISK LADLE PANTRY</span>
    </div>
    <div class="line-name">Brisk Toppings</div>

    <div class="story">
      <p>Life's too short to dress a great salad with a dressing that doesn't cut the mustard. This dress has been a favorite of friends and family for years. We hope it becomes yours.</p>
      <p><strong>Foodie Tip:</strong> Get Crazy.<br>Marinade your chicken and seafood with this dressing and earn bragging rights.</p>
    </div>

    <div class="title">
      <div class="title-top">ARTISAN</div>
      <div class="title-main">VINAIGRETTE</div>
    </div>
    <div class="title-rule"></div>

    <div class="marinade-band"></div>
    <div class="marinade">&amp; MARINADE</div>

    <div class="ingredients"><b>Ingredients:</b> vinegar, olive oil, dijon mustard, fondor, xanthan gum <b>Allergens:</b> Soy</div>

    <div class="nutrition-panel"></div>
    <div class="nutrition">
      <b>Nutrition Facts</b><br>
      Serving size: 1 TBS Vinaigrette (15.3g)<br>
      <b>Amount per serving</b>
      <div class="row"><span><b>Calories</b> 51</span><span>Calories from Fat 48</span></div>
      <div class="row"><span></span><b>% Daily Values*</b></div>
      <div class="rule"></div>
      <div class="row"><span><b>Total Fat</b> 5g</span><span>7%</span></div>
      <div class="row indent"><span>Saturated Fat 0g</span><span>2%</span></div>
      <div class="indent">Trans Fat 0g</div>
      <div class="row"><span><b>Cholesterol</b> 0mg</span><span>0%</span></div>
      <div class="row"><span><b>Sodium</b> 141mg</span><span>6%</span></div>
      <div class="row"><span><b>Total Carbohydrate</b> 0g</span><span>0%</span></div>
      <div class="row indent"><span>Dietary Fiber 0g</span><span>0%</span></div>
      <div class="indent">Sugars 0g</div>
      <div><b>Protein</b> 0g</div>
      <div class="row"><span>Vitamin A 0%</span><span>Calcium 0%</span></div>
      <div class="row"><span>Vitamin C 0%</span><span>Iron 0%</span></div>
      *Percent Daily Values are based on a 2,000 calorie diet.
    </div>

    <div class="gray-bar"></div>
    <div class="green-bar"></div>
    <div class="lower-stripes"></div>
    <div class="salad-art" role="img" aria-label="Bowl of fresh garden salad"></div>
    <div class="fork-art" role="img" aria-label="Silver fork beside the salad bowl"></div>

    <div class="care-left">Give me a good shake before enjoying.<br>Made in Small Batches because we can.</div>
    <div class="thanks">Thanks for trusting us with your appetite!<br>savour the experience... ™</div>
    <div class="net">NET 8 FL<br>OZ (237 ML)</div>
    <div class="care-right">
      For recipe ideas and questions visit:
      <span class="web">www.briskladlepantry.com</span>
      <div class="storage">Refrigerate after opening.<br>Best served at room temperature.</div>
    </div>
  </div>
</body>
</html>
```